Business Card and Stationary for Construction Company
RT Hollis Construction
Professional
Marcus Hollis
General Contractor
Serving Harbor Valley
rthollis.build@examplemail.net
License #417862

```html
<!DOCTYPE html>
<html lang="en">
<head>
<meta charset="utf-8">
<title>RT Hollis Construction – Business Card</title>
<link rel="stylesheet" href="https://fonts.googleapis.com/css2?family=Cinzel:wght@400&display=swap">
<style>
  :root {
    --page-bg: #e6e6e6;
    --card-bg: #ffffff;
    --brand-red: #c4161c;
    --brand-red-deep: #8a0c10;
    --swoosh-dark: #3a3a3a;
    --swoosh-light: #9a9a9a;
    --text-grey: #555555;
    --text-dark: #3c3c3c;
    --text-white: #ffffff;
  }
  * { box-sizing: border-box; margin: 0; padding: 0; }
  html, body {
    width: 1200px;
    height: 991px;
    overflow: hidden;
    background: var(--page-bg);
  }
  .sheet {
    width: 1200px;
    height: 991px;
    display: flex;
    flex-direction: column;
    align-items: center;
    justify-content: center;
    gap: 70px;
  }
  .card {
    width: 640px;
    height: 366px;
    border-radius: 26px;
    background: var(--card-bg);
    overflow: hidden;
    box-shadow: 0 6px 18px rgba(0,0,0,0.18);
    position: relative;
  }
  .card svg { display: block; }
  .card-text { font-family: "Cinzel", serif; }
  .contact-line { fill: var(--text-white); font-size: 11px; letter-spacing: 0.4px; }
  .contact-icon { fill: none; stroke: var(--text-white); stroke-width: 1.2; }
  .company-name { fill: var(--text-dark); font-weight: 400; letter-spacing: 1px; }
  .person-name { fill: var(--text-grey); font-size: 15px; letter-spacing: 1px; }
  .person-title { fill: var(--text-grey); font-size: 13px; letter-spacing: 0.8px; }
  .web-address { fill: var(--text-grey); font-size: 12px; letter-spacing: 3px; }
</style>
</head>
<body>
<main class="sheet">

  <section class="card card-back" aria-label="Business card back">
    <svg width="640" height="366" viewBox="0 0 640 366" class="card-text">
      <text class="company-name" x="320" y="175" font-size="22" text-anchor="middle">RT Hollis Construction</text>
      <text class="web-address" x="320" y="225" text-anchor="middle">WWW.RTHOLLIS-BUILD.EXAMPLE</text>
    </svg>
  </section>

  <section class="card card-front" aria-label="Business card front">
    <svg width="640" height="366" viewBox="0 0 640 366" class="card-text">
      <defs>
        <linearGradient id="band-red" x1="0" y1="0" x2="1" y2="1">
          <stop offset="0" stop-color="var(--brand-red)"/>
          <stop offset="1" stop-color="var(--brand-red-deep)"/>
        </linearGradient>
        <linearGradient id="band-swoosh" x1="0" y1="0" x2="1" y2="0">
          <stop offset="0" stop-color="var(--swoosh-light)"/>
          <stop offset="0.5" stop-color="var(--swoosh-dark)"/>
          <stop offset="1" stop-color="var(--swoosh-light)"/>
        </linearGradient>
      </defs>

      <path class="swoosh" d="M0,108 C170,112 360,205 475,366 L445,366 C340,222 165,128 0,124 Z" fill="url(#band-swoosh)"/>
      <path class="red-band" d="M0,132 C160,140 335,232 432,366 L0,366 Z" fill="url(#band-red)"/>

      <g class="contact-list">
        <circle class="contact-icon" cx="28" cy="206" r="5"/>
        <text class="contact-line" x="40" y="210">Serving Harbor Valley</text>
        <circle class="contact-icon" cx="28" cy="230" r="5"/>
        <text class="contact-line" x="40" y="234">P (555) 201-4478</text>
        <circle class="contact-icon" cx="28" cy="254" r="5"/>
        <text class="contact-line" x="40" y="258">F (555) 201-4479</text>
        <circle class="contact-icon" cx="28" cy="278" r="5"/>
        <text class="contact-line" x="40" y="282">rthollis.build@examplemail.net</text>
        <circle class="contact-icon" cx="28" cy="302" r="5"/>
        <text class="contact-line" x="40" y="306">License #417862</text>
      </g>

      <text class="company-name" x="600" y="150" font-size="22" text-anchor="end">RT Hollis Construction</text>

      <text class="person-name" x="600" y="312" text-anchor="end">Marcus Hollis</text>
      <text class="person-title" x="600" y="332" text-anchor="end">General Contractor</text>
    </svg>
  </section>

</main>
</body>
</html>
```